【 概要 】 動物病院の診察券リニューアルに伴い、新しいデザインを募集します。 今回は「飼い主様が持ちたくなる、ひと目でペットの種類がわかるデザイン」を目指しています。【 依頼内容 】 作成数: 3種類(犬、猫、小動物) サイズ: 横 約85.6mm × 縦 約54mm(一般的なクレジットカードサイズ) 利用用途:診察券 【 デザイン詳細 】 1. 表面(イラスト面)について 文字情報は一切入れず、動物のイラストを主役にしたデザインをお願いします。 ■種類の強調: 「犬」「猫」「小動物」それぞれの品種を大きく目立たせてください。 ■小動物カードの構成: 主に小動物は「うさぎ、ハムスター、チンチラ、ハリネズミ」を診察します (4種類をバランスよく配置、もしくは集合しているイラストなど)。 ■色分け: それぞれベースカラーを変えて視覚的に区別しやすくしてください。 ■雰囲気: 清潔感があり、優しく、親しみやすい雰囲気 ■参考: 現在はモコふわデザインを使用。それよりも「どの動物のカードか」がより直感的に伝わるデザインを求めています。 2. 裏面(情報面)について 裏面には、病院名、診察券番号、飼い主名、ペット名、診療時間表などの情報を掲載します。 掲載内容:添付のファイル(資料)をご確認ください。 【 契約金額(税抜) 】 5万円 ※契約金額(税込)からシステム利用料を差し引いた金額が、ワーカーさまの受取金額となります。 その他ご質問等ありましたら、気軽にお問い合わせください。 ご応募をお待ちしております! |
| https://www.kiriha-vet.jp/ | ||
どの案も素敵でしたが、こちらのデザインが当院のイメージにあっていました。
皆様ご提案ありがとうございました。
どれも個性的で良い提案ばかりでした。
また機会があれば依頼させていただきますのでよろしくお願いいたします。

```html
<!DOCTYPE html>
<html lang="ja">
<head>
<meta charset="utf-8">
<title>診察券デザイン 犬・猫・小動物</title>
<link rel="stylesheet" href="https://fonts.googleapis.com/css2?family=Noto+Sans+JP:wght@400;500;700;900&display=swap">
<style>
:root{
  --page:#ffffff;
  --dog:#6b1616;
  --cat:#7d6257;
  --small:#2f4a2b;
  --ink:#2a2a2a;
  --rule:#bdbdbd;
  --card-w:440px;
  --card-h:280px;
}
*{box-sizing:border-box;margin:0;padding:0}
html,body{width:1200px;height:1154px;overflow:hidden;background:var(--page)}
body{position:relative;font-family:"Noto Sans JP",sans-serif;color:var(--ink)}

.card-set{position:absolute;left:0;width:1200px}
.set-dog{top:0;--accent:var(--dog)}
.set-cat{top:392px;--accent:var(--cat)}
.set-small{top:794px;--accent:var(--small)}

.card-front{
  position:absolute;left:110px;top:6px;
  width:var(--card-w);height:var(--card-h);
  background:var(--accent);
  display:flex;align-items:center;justify-content:center;
}
.illustration{
  width:250px;height:140px;border-radius:18px;
  background:radial-gradient(ellipse at center,rgba(255,255,255,.32),rgba(255,255,255,.1) 70%,rgba(255,255,255,0));
}
.set-small .illustration{width:300px;height:190px}

.card-back{
  position:absolute;left:638px;top:0;
  width:554px;height:350px;
  background:#fff;border:1.5px solid var(--rule);
  padding:24px 26px 0 26px;
  color:var(--accent);
}
.karte{
  font-size:16px;font-weight:500;color:var(--ink);
  padding-bottom:6px;border-bottom:1.5px solid var(--accent);
}
.owner{
  margin-top:30px;display:flex;font-size:16px;font-weight:500;color:var(--ink);
  padding-bottom:5px;border-bottom:1.5px solid var(--accent);
}
.owner .name-label{width:185px}
.owner .honorific{width:40px}
.owner .pet-label{flex:1}
.clinic{
  margin-top:14px;display:flex;align-items:center;gap:16px;
}
.clinic-name{font-size:23px;font-weight:900;letter-spacing:.02em;color:var(--accent)}
.clinic-phone{display:flex;align-items:center;gap:4px;font-size:18px;font-weight:700;color:var(--accent)}
.clinic-phone svg{width:20px;height:20px;fill:var(--accent)}

.hours{
  margin-top:6px;width:100%;border-collapse:separate;border-spacing:0 3px;
  font-size:17px;font-weight:700;
}
.hours th,.hours td{height:27px;text-align:center;vertical-align:middle}
.hours thead th{background:var(--accent);color:#fff;font-weight:700}
.hours thead th.slot{letter-spacing:.3em;width:170px}
.hours tbody th{background:var(--accent);color:#fff;font-weight:700;letter-spacing:.03em}
.hours td{position:relative;color:var(--accent)}
.dot{display:inline-block;width:14px;height:14px;border-radius:50%;background:var(--accent);vertical-align:middle}
.closed{font-weight:400;font-size:20px}
.mark{position:absolute;right:-4px;top:2px;font-size:9px;font-weight:700}

.notes{margin-top:4px;font-size:14px;font-weight:500;line-height:1.35;color:var(--accent)}
</style>
</head>
<body>

<section class="card-set set-dog" aria-label="犬用診察券">
  <div class="card-front"><div class="illustration" role="img" aria-label="白いハートと犬のシルエットのイラスト"></div></div>
  <div class="card-back">
    <p class="karte">カルテ No.</p>
    <p class="owner"><span class="name-label">氏名</span><span class="honorific">様</span><span class="pet-label">ペット名</span><span>ちゃん</span></p>
    <div class="clinic">
      <span class="clinic-name">桐葉動物医療センター</span>
      <span class="clinic-phone"><svg viewBox="0 0 24 24" aria-hidden="true"><path d="M6.6 10.8a15.1 15.1 0 0 0 6.6 6.6l2.2-2.2a1 1 0 0 1 1-.25 11.4 11.4 0 0 0 3.6.57 1 1 0 0 1 1 1V20a1 1 0 0 1-1 1A17 17 0 0 1 3 4a1 1 0 0 1 1-1h3.5a1 1 0 0 1 1 1c0 1.25.2 2.45.57 3.57a1 1 0 0 1-.25 1z"/></svg>本院 086-555-0142</span>
    </div>
    <table class="hours">
      <thead><tr><th class="slot">診療時間</th><th>月</th><th>火</th><th>水</th><th>木</th><th>金</th><th>土</th></tr></thead>
      <tbody>
        <tr><th>9：00～11：30</th><td><span class="dot"></span></td><td><span class="dot"></span></td><td><span class="dot"></span></td><td class="closed">／</td><td><span class="dot"></span></td><td><span class="dot"></span><span class="mark">※1</span></td></tr>
        <tr><th>16：00～18：30</th><td><span class="dot"></span></td><td><span class="dot"></span></td><td><span class="dot"></span></td><td class="closed">／</td><td><span class="dot"></span></td><td><span class="dot"></span><span class="mark">※2</span></td></tr>
      </tbody>
    </table>
    <p class="notes">※1 土曜日午前は 9：00～12：30。<br>※2 土曜日午後は 14:00～18:30、予約診療のみとなります。</p>
  </div>
</section>

<section class="card-set set-cat" aria-label="猫用診察券">
  <div class="card-front"><div class="illustration" role="img" aria-label="白いハートと猫のシルエットのイラスト"></div></div>
  <div class="card-back">
    <p class="karte">カルテ No.</p>
    <p class="owner"><span class="name-label">氏名</span><span class="honorific">様</span><span class="pet-label">ペット名</span><span>ちゃん</span></p>
    <div class="clinic">
      <span class="clinic-name">桐葉動物医療センター</span>
      <span class="clinic-phone"><svg viewBox="0 0 24 24" aria-hidden="true"><path d="M6.6 10.8a15.1 15.1 0 0 0 6.6 6.6l2.2-2.2a1 1 0 0 1 1-.25 11.4 11.4 0 0 0 3.6.57 1 1 0 0 1 1 1V20a1 1 0 0 1-1 1A17 17 0 0 1 3 4a1 1 0 0 1 1-1h3.5a1 1 0 0 1 1 1c0 1.25.2 2.45.57 3.57a1 1 0 0 1-.25 1z"/></svg>本院 086-555-0142</span>
    </div>
    <table class="hours">
      <thead><tr><th class="slot">診療時間</th><th>月</th><th>火</th><th>水</th><th>木</th><th>金</th><th>土</th></tr></thead>
      <tbody>
        <tr><th>9：00～11：30</th><td><span class="dot"></span></td><td><span class="dot"></span></td><td><span class="dot"></span></td><td class="closed">／</td><td><span class="dot"></span></td><td><span class="dot"></span><span class="mark">※1</span></td></tr>
        <tr><th>16：00～18：30</th><td><span class="dot"></span></td><td><span class="dot"></span></td><td><span class="dot"></span></td><td class="closed">／</td><td><span class="dot"></span></td><td><span class="dot"></span><span class="mark">※2</span></td></tr>
      </tbody>
    </table>
    <p class="notes">※1 土曜日午前は 9：00～12：30。<br>※2 土曜日午後は 14:00～18:30、予約診療のみとなります。</p>
  </div>
</section>

<section class="card-set set-small" aria-label="小動物用診察券">
  <div class="card-front"><div class="illustration" role="img" aria-label="白いハートとうさぎ・ハムスター・チンチラ・ハリネズミのシルエットのイラスト"></div></div>
  <div class="card-back">
    <p class="karte">カルテ No.</p>
    <p class="owner"><span class="name-label">氏名</span><span class="honorific">様</span><span class="pet-label">ペット名</span><span>ちゃん</span></p>
    <div class="clinic">
      <span class="clinic-name">桐葉動物医療センター</span>
      <span class="clinic-phone"><svg viewBox="0 0 24 24" aria-hidden="true"><path d="M6.6 10.8a15.1 15.1 0 0 0 6.6 6.6l2.2-2.2a1 1 0 0 1 1-.25 11.4 11.4 0 0 0 3.6.57 1 1 0 0 1 1 1V20a1 1 0 0 1-1 1A17 17 0 0 1 3 4a1 1 0 0 1 1-1h3.5a1 1 0 0 1 1 1c0 1.25.2 2.45.57 3.57a1 1 0 0 1-.25 1z"/></svg>本院 086-555-0142</span>
    </div>
    <table class="hours">
      <thead><tr><th class="slot">診療時間</th><th>月</th><th>火</th><th>水</th><th>木</th><th>金</th><th>土</th></tr></thead>
      <tbody>
        <tr><th>9：00～11：30</th><td><span class="dot"></span></td><td><span class="dot"></span></td><td><span class="dot"></span></td><td class="closed">／</td><td><span class="dot"></span></td><td><span class="dot"></span><span class="mark">※1</span></td></tr>
        <tr><th>16：00～18：30</th><td><span class="dot"></span></td><td><span class="dot"></span></td><td><span class="dot"></span></td><td class="closed">／</td><td><span class="dot"></span></td><td><span class="dot"></span><span class="mark">※2</span></td></tr>
      </tbody>
    </table>
    <p class="notes">※1 土曜日午前は 9：00～12：30。<br>※2 土曜日午後は 14:00～18:30、予約診療のみとなります。</p>
  </div>
</section>

</body>
</html>
```